Varnelle 514xt – BrightLane branding

Our company offers very affordable internet access and television using our own Fiber network. To gain more brand awareness we would like to wrap the cars starting with my own (pearl white) Varnelle 514xt (Cabrio).
Design should be neat / business, but attract people..
A design can be an include our pricing (not required):
Gigabit glasvezel €17,95 per maand
But if it's included in the design it needs to be easily / affordable changeable (since pricing might change in the future).
Attached our logo and some flyers to give an impression of our corporate identity.
Our main competitors are:
- DRV (Grand Lowland Signalworks)
- Pomra / Teralink (Meridian Holdco)
- Q-Cellnet
The current color of the car is (pearl) white, in my opinion a partial wrap could be enough, but if you think a full wrap might work better for your design feel free to submit that :-)
Industry/Entity Type
FttH - Internet Service Provider
Look and feel

```html
<!DOCTYPE html>
<html lang="nl">
<head>
<meta charset="utf-8">
<title>Varnelle 514xt – BrightLane car wrap</title>
<link rel="stylesheet" href="https://fonts.googleapis.com/css2?family=Oswald:wght@500;600&display=swap">
<style>
  :root {
    --wrap-blue: #1459ad;
    --wrap-orange: #e66d3d;
    --wrap-green: #5e8c55;
    --pearl-white: #ffffff;
    --vehicle-tone: #eef0f3;
    --canvas-bg: #ffffff;
  }
  html, body {
    margin: 0;
    width: 1200px;
    height: 1000px;
    overflow: hidden;
    background: var(--canvas-bg);
  }
  .wrap-sheet {
    display: block;
    width: 1200px;
    height: 1000px;
    font-family: "Oswald", sans-serif;
  }
  .vehicle-placeholder { fill: var(--vehicle-tone); }
  .rear-field { fill: var(--wrap-blue); }
  .stripe-blue { fill: none; stroke: var(--wrap-blue); stroke-width: 12; }
  .stripe-orange { fill: none; stroke: var(--wrap-orange); stroke-width: 10; }
  .brand-dot { fill: var(--wrap-blue); }
  .brand-name { fill: var(--wrap-blue); font-size: 38px; font-weight: 500; }
  .price-disc { fill: var(--pearl-white); }
  .price-arc { fill: none; stroke: var(--wrap-orange); stroke-width: 4; }
  .price-amount { fill: var(--wrap-blue); font-size: 22px; font-weight: 600; }
  .tag-orange { fill: var(--wrap-orange); }
  .tag-white { fill: var(--pearl-white); }
  .tag-text-light { fill: var(--pearl-white); font-size: 16px; font-weight: 600; }
  .tag-text-green { fill: var(--wrap-green); font-size: 16px; font-weight: 600; }
  .tag-rule { stroke: var(--wrap-blue); stroke-width: 3; }
</style>
</head>
<body>
<svg class="wrap-sheet" viewBox="0 0 1200 1000" xmlns="http://www.w3.org/2000/svg">
  <defs>
    <g id="livery">
      <rect class="vehicle-placeholder" x="18" y="185" width="1147" height="255" rx="18" role="img" aria-label="Pearl white Varnelle 514xt cabrio, side view"/>
      <path class="rear-field" d="M772,200 L1165,200 L1165,440 L600,440 C625,428 638,418 648,405 C690,355 708,255 772,200 Z"/>
      <path class="stripe-blue" d="M728,203 C662,252 642,340 592,386 C572,403 550,415 520,415 L295,415"/>
      <path class="stripe-orange" d="M750,203 C684,256 664,352 614,400 C592,420 566,437 530,437 L295,437"/>
    </g>
  </defs>

  <g class="car car--left-side">
    <use href="#livery"/>
    <g class="brand-mark">
      <circle class="brand-dot" cx="410" cy="322" r="13"/>
      <text class="brand-name" x="430" y="336">BrightLane</text>
    </g>
    <g class="price-badge">
      <circle class="price-disc" cx="775" cy="268" r="42"/>
      <path class="price-arc" d="M745,292 A38,38 0 0 0 812,280"/>
      <text class="price-amount" x="775" y="276" text-anchor="middle">€17,95</text>
      <rect class="tag-orange" x="822" y="230" width="140" height="26"/>
      <text class="tag-text-light" x="828" y="249" textLength="128" lengthAdjust="spacingAndGlyphs">GIGABIT GLASVEZEL</text>
      <line class="tag-rule" x1="822" y1="262" x2="940" y2="262"/>
      <rect class="tag-white" x="822" y="266" width="92" height="24"/>
      <text class="tag-text-green" x="868" y="284" text-anchor="middle">PER MAAND</text>
    </g>
  </g>

  <g class="car car--right-side">
    <use href="#livery" transform="translate(1200,485) scale(-1,1)"/>
    <g class="brand-mark">
      <circle class="brand-dot" cx="628" cy="807" r="13"/>
      <text class="brand-name" x="648" y="821">BrightLane</text>
    </g>
    <g class="price-badge">
      <circle class="price-disc" cx="425" cy="755" r="42"/>
      <path class="price-arc" d="M455,779 A38,38 0 0 1 388,767"/>
      <text class="price-amount" x="425" y="763" text-anchor="middle">€17,95</text>
      <rect class="tag-orange" x="232" y="717" width="140" height="26"/>
      <text class="tag-text-light" x="238" y="736" textLength="128" lengthAdjust="spacingAndGlyphs">GIGABIT GLASVEZEL</text>
      <line class="tag-rule" x1="254" y1="749" x2="372" y2="749"/>
      <rect class="tag-white" x="280" y="753" width="92" height="24"/>
      <text class="tag-text-green" x="326" y="771" text-anchor="middle">PER MAAND</text>
    </g>
  </g>
</svg>
</body>
</html>
```